Business Card Design Project For Moving Company

Hello,

We need the business card to be 2 sided and we were thinking to use the logo on the front of the card (see file 1 attached) and the text "logo" (see file 2 attached) in the back of the card. We're looking for a powerful design that will help us build our brand, as our company is new.
We are a full service moving company (no storage) located in San Diego, CA, USA. The design should communicate to our potential customers that we have the highest level of service, customer satisfaction is our number one goal, our team is professional and efficient.

Thank you,

Gil
Updates

Project Deadline Extended
Reason: We would like to have more time to provide feedback for the designs already submitted. Thank you, Gil

Industry/Entity Type

Moving Company

Requirements
Must have
• Front of the card must have the following text and logo:
Haul Brightway, Inc
Residential And Commercial
Local And Long Distance
Address: 3917 Alder Crest Rd, #412,
San Diego, CA, 92087
P: 855-372-LIFT (5438)
F: 858-291-4476
info@haul-brightway.com
www.haul-brightway.com

Back of the card must have the following text and text "logo" (file 2 attached):

The best compliment we can ever receive is a referral from our clients.

```html
<!DOCTYPE html>
<html lang="en">
<head>
<meta charset="utf-8">
<title>Haul Brightway, Inc – Business Card</title>
<link rel="stylesheet" href="https://fonts.googleapis.com/css2?family=Exo+2:wght@300;400;600;800&display=swap">
<style>
  :root {
    --backdrop: #d9d6d1;
    --card: #f4f5f7;
    --card-edge: #e4e6ea;
    --ink: #2b2d31;
    --ink-soft: #4a4c52;
    --accent: #d4231c;
    --photo-sky: #8fa4ad;
    --photo-road: #4d5356;
    --photo-glow: #e7b37a;
  }
  * { margin: 0; padding: 0; box-sizing: border-box; }
  html, body {
    width: 1200px; height: 803px; overflow: hidden;
    background: var(--backdrop);
    font-family: "Exo 2", sans-serif;
    color: var(--ink);
  }
  .canvas { position: relative; width: 1200px; height: 803px; }

  .card {
    position: absolute;
    width: 560px; height: 322px;
    background: var(--card);
    border: 1px solid var(--card-edge);
    box-shadow: 0 6px 16px rgba(0,0,0,.25);
    overflow: hidden;
  }

  /* Front */
  .card-front { left: 70px; top: 100px; display: flex; }
  .front-photo {
    width: 241px; height: 100%;
    background:
      radial-gradient(circle at 10% 35%, var(--photo-glow) 0, rgba(231,179,122,0) 35%),
      linear-gradient(180deg, var(--photo-sky) 0%, #a7b4b8 45%, var(--photo-road) 100%);
  }
  .front-info { flex: 1; padding: 26px 0 0 24px; }
  .company-name {
    font-weight: 600; font-size: 14px; line-height: 18px; letter-spacing: .3px;
    color: var(--accent);
    margin-bottom: 12px;
  }
  .tagline {
    font-weight: 400; font-size: 18px; line-height: 25px; letter-spacing: .2px;
    width: 256px;
  }
  .divider {
    width: 256px; height: 2px;
    background: var(--accent);
    margin-top: 8px;
  }
  .contact-list { list-style: none; margin-top: 14px; }
  .contact-item {
    display: flex; align-items: flex-start;
    font-weight: 300; font-size: 16px; line-height: 23px; color: var(--ink-soft);
  }
  .contact-icon { width: 14px; height: 14px; margin: 4px 9px 0 0; flex: none; }
  .contact-icon.blank { visibility: hidden; }

  /* Back */
  .card-back {
    left: 570px; top: 430px;
    display: flex; flex-direction: column; align-items: center; justify-content: center;
    gap: 22px;
    background: linear-gradient(135deg, #ffffff 0%, var(--card) 100%);
  }
  .brand-name {
    font-weight: 800; font-size: 50px; letter-spacing: 1px;
    text-transform: uppercase; color: var(--accent);
  }
  .referral-quote {
    font-weight: 300; font-size: 15px; line-height: 21px;
    color: var(--ink-soft); text-align: center;
    width: 420px;
  }
</style>
</head>
<body>
<main class="canvas">

  <section class="card card-front" aria-label="Business card front">
    <div class="front-photo" role="img" aria-label="Photograph of a semi truck speeding along a highway"></div>
    <div class="front-info">
      <p class="company-name">Haul Brightway, Inc</p>
      <p class="tagline">Residential And Commercial<br>Local And Long Distance</p>
      <div class="divider"></div>
      <ul class="contact-list">
        <li class="contact-item">
          <svg class="contact-icon" viewBox="0 0 14 14"><circle cx="7" cy="7" r="6" fill="none" stroke="#2b2d31" stroke-width="1.5"/><circle cx="7" cy="7" r="3" fill="#2b2d31"/></svg>
          <span>3917 Alder Crest Rd, #412,<br>San Diego, CA, 92087</span>
        </li>
        <li class="contact-item">
          <svg class="contact-icon" viewBox="0 0 14 14"><rect x="4" y="1" width="6" height="12" rx="1" fill="none" stroke="#2b2d31" stroke-width="1.4"/><rect x="5.5" y="3" width="3" height="4" fill="#d4231c"/></svg>
          <span>P: 855-372-LIFT (5438)</span>
        </li>
        <li class="contact-item">
          <svg class="contact-icon blank" viewBox="0 0 14 14"></svg>
          <span>F: 858-291-4476</span>
        </li>
        <li class="contact-item">
          <svg class="contact-icon" viewBox="0 0 14 14"><text x="7" y="12" text-anchor="middle" font-size="14" font-weight="700" fill="#2b2d31" font-family="sans-serif">@</text></svg>
          <span>info@haul-brightway.com</span>
        </li>
        <li class="contact-item">
          <svg class="contact-icon" viewBox="0 0 14 14"><rect x="1" y="1.5" width="12" height="8" fill="none" stroke="#2b2d31" stroke-width="1.4"/><rect x="5" y="10" width="4" height="1.5" fill="#2b2d31"/><rect x="3.5" y="11.5" width="7" height="1.2" fill="#2b2d31"/></svg>
          <span>www.haul-brightway.com</span>
        </li>
      </ul>
    </div>
  </section>

  <section class="card card-back" aria-label="Business card back">
    <p class="brand-name">Haul Brightway</p>
    <p class="referral-quote">The best compliment we can ever receive is a referral from our clients.</p>
  </section>

</main>
</body>
</html>
```